Corwin Ashdale Building Company, Inc.
Business Cards, Letterhead, Envelopes, Fax Cover
Professional
Miles T. Fenwick
PO Box 48217
Fernwood, NC 27690
miles@corwinashdale-example.com
www.corwinashdale-example.com
looking for a traditional style card, however nothing dated. same goes for the stationary. Something that is creative , but still shows professionalism and adaptable to the corporate environment. We don't want gloss cards. waiting on office and fax #'s. should have those in a day or two. As for the font, I put use same as logo font, but may want to see standard as well.
CA

```html
<!DOCTYPE html>
<html lang="en">
<head>
<meta charset="utf-8">
<title>Corwin Ashdale Building Company – Business Card</title>
<link rel="stylesheet" href="https://fonts.googleapis.com/css2?family=Raleway:wght@400&family=Arimo:wght@400&display=swap">
<style>
  :root {
    --backdrop: #7a5230;
    --card: #ffffff;
    --navy: #1d3461;
    --band-dark: #15264a;
    --band-light: #2f5a9e;
    --ink: #333a45;
    --muted: #666c75;
  }
  * { margin: 0; padding: 0; box-sizing: border-box; }
  html, body { width: 1200px; height: 367px; overflow: hidden; }
  body { background: var(--backdrop); position: relative; font-family: "Arimo", Arial, sans-serif; }
  .card {
    position: absolute; top: 34px; width: 561px; height: 302px;
    background: var(--card); border-radius: 22px; overflow: hidden;
    box-shadow: 0 2px 6px rgba(0,0,0,.25);
  }
  .card--front { left: 29px; }
  .card--back { left: 614px; }
  .band { position: absolute; left: 0; top: 0; width: 36px; height: 302px; }
  .band-icons { position: absolute; left: 14px; top: 208px; display: flex; flex-direction: column; gap: 9px; }
  .band-icons span { width: 8px; height: 8px; border-radius: 50%; background: #ffffff; opacity: .85; }
  .mark { position: absolute; background: var(--navy); }
  .card--front .mark { left: 48px; top: 46px; width: 50px; height: 52px; }
  .card--back .mark { left: 84px; top: 110px; width: 56px; height: 60px; }
  .wordmark { position: absolute; font-family: "Raleway", Arial, sans-serif; font-weight: 400; color: var(--navy); line-height: 1; white-space: nowrap; }
  .wordmark .line1, .wordmark .line2 { display: block; text-transform: uppercase; }
  .card--front .wordmark { left: 116px; top: 48px; }
  .card--front .line1 { font-size: 30px; letter-spacing: .5px; }
  .card--front .line2 { font-size: 16px; letter-spacing: 5px; margin-top: 6px; }
  .card--back .wordmark { left: 152px; top: 112px; }
  .card--back .line1 { font-size: 34px; letter-spacing: .6px; }
  .card--back .line2 { font-size: 18px; letter-spacing: 5.6px; margin-top: 8px; }
  .contact { position: absolute; left: 40px; top: 120px; font-size: 12.5px; line-height: 17px; color: var(--ink); list-style: none; }
  .contact .gap { margin-top: 12px; }
  .person { position: absolute; left: 360px; top: 198px; width: 150px; text-align: center; color: var(--ink); }
  .person .name { font-size: 15px; }
  .person .role { font-size: 12px; color: var(--muted); margin-top: 14px; }
  .web { position: absolute; left: 196px; top: 258px; font-size: 12.5px; color: var(--ink); display: flex; align-items: center; gap: 8px; }
  .web .dot { width: 10px; height: 10px; border-radius: 50%; background: var(--navy); }
</style>
</head>
<body>
  <section class="card card--front">
    <svg class="band" viewBox="0 0 36 302" aria-hidden="true">
      <defs>
        <linearGradient id="bandFill" x1="0" y1="0" x2="1" y2="0">
          <stop offset="0" stop-color="#15264a"/>
          <stop offset="1" stop-color="#2f5a9e"/>
        </linearGradient>
      </defs>
      <path d="M0 0 H34 Q28 151 34 302 H0 Z" fill="url(#bandFill)"/>
    </svg>
    <div class="band-icons" aria-hidden="true"><span></span><span></span><span></span></div>
    <div class="mark" aria-hidden="true"></div>
    <div class="wordmark">
      <span class="line1">Corwin Ashdale</span>
      <span class="line2">Building Company</span>
    </div>
    <ul class="contact">
      <li>PO Box 48217</li>
      <li>Fernwood, NC 27690</li>
      <li class="gap">123-456-7890</li>
      <li>919-555-0148</li>
      <li>123-456-7890</li>
      <li>miles@corwinashdale-example.com</li>
      <li>www.corwinashdale-example.com</li>
    </ul>
    <div class="person">
      <p class="name">Miles T. Fenwick</p>
      <p class="role">Principal</p>
    </div>
  </section>

  <section class="card card--back">
    <div class="mark" aria-hidden="true"></div>
    <div class="wordmark">
      <span class="line1">Corwin Ashdale</span>
      <span class="line2">Building Company</span>
    </div>
    <p class="web"><span class="dot"></span>www.corwinashdale-example.com</p>
  </section>
</body>
</html>
```